Enhancement Of Draft Website - www.skyvoltbridge.net

The website www.skyvoltbridge.net exists but needs further development. With the exception of a small number of pages, the website is populated with the majority of content it requires. I would like a designer to review the design of the website and propose an enhanced design paying particular consideration to the following:

-Setting an appropriate colour scheme that matches with the company logo
-Ensuring the company logo is displayed appropriately on the website
-Making any other appropriate adjustments (through the selection of another theme / the customisation of the existing template) that improve the experience of the user on the website

An XML export file from the existing website is attached.

Target Market(s)

Specialist website targeting engineers working in aerospace companies

Industry/Entity Type

Engineer

Font styles to use
Sans Serif

Requirements
Must have
• Responsive design working across platforms. Contact form. Ease of use.

```html
<!DOCTYPE html>
<html lang="en">
<head>
<meta charset="utf-8">
<title>skyvoltbridge – High Voltage Engineering</title>
<link href="https://fonts.googleapis.com/css2?family=Oswald:wght@400;500&family=Roboto:wght@400;500&display=swap" rel="stylesheet">
<style>
:root{
  --brand:#3a6a96;
  --brand-dark:#2e5b86;
  --ink:#222;
  --muted:#777;
  --footer:#2b2b2b;
  --footer-bottom:#232323;
  --white:#fff;
}
*{margin:0;padding:0;box-sizing:border-box}
html,body{width:1200px;height:2195px;overflow:hidden}
body{font-family:"Roboto",Arial,sans-serif;color:var(--ink);background:var(--white);position:relative}
a{color:inherit;text-decoration:none}

.topbar{position:absolute;top:0;left:0;width:1200px;height:37px;background:var(--brand);color:var(--white);font-size:13px}
.topbar .contact{position:absolute;left:91px;top:11px;display:flex;gap:26px}
.topbar .contact span{display:flex;align-items:center;gap:6px}
.topbar .search{position:absolute;left:978px;top:10px}
.topbar .divider{position:absolute;left:1007px;top:0;width:1px;height:37px;background:rgba(255,255,255,.35)}
.topbar .social{position:absolute;left:1032px;top:13px;display:flex;gap:5px}
.topbar .social i{width:12px;height:12px;background:var(--white);border-radius:2px;display:block}

.header{position:absolute;top:37px;left:0;width:1200px;height:88px;background:var(--white)}
.brand{position:absolute;left:91px;top:26px;display:flex;align-items:center;gap:10px;font-size:30px;font-weight:500;color:var(--brand-dark)}
.brand i{width:30px;height:30px;background:var(--brand-dark);display:block}
.nav{position:absolute;right:85px;top:40px;display:flex;gap:38px;font-size:13.5px;color:#333}
.nav a.active{color:var(--brand)}

.hero{position:absolute;top:125px;left:0;width:1200px;height:582px;background:radial-gradient(ellipse at 50% 35%,#55606a 0%,#2d343b 55%,#15191d 100%)}
.hero h1{position:absolute;top:210px;width:100%;text-align:center;font-family:"Oswald",sans-serif;font-weight:400;font-size:58px;color:var(--white);letter-spacing:.5px;text-shadow:0 2px 6px rgba(0,0,0,.6)}
.hero p{position:absolute;top:285px;width:100%;text-align:center;font-family:"Oswald",sans-serif;font-size:28px;color:var(--white);text-shadow:0 2px 6px rgba(0,0,0,.6)}
.hero .arrow{position:absolute;top:267px;width:30px;height:30px;border-radius:50%;background:rgba(0,0,0,.55)}
.hero .arrow svg{display:block}

.tiles{position:absolute;top:707px;left:0;width:1200px;height:297px;display:flex}
.tile{flex:1;position:relative}
.tile:nth-child(1){background:linear-gradient(135deg,#5a5a55,#2a4e8c 70%,#222)}
.tile:nth-child(2){background:linear-gradient(180deg,#c8ccd0,#6b6e72)}
.tile:nth-child(3){background:radial-gradient(ellipse at 50% 40%,#8aa2ff,#2b2f8a 55%,#0d0f30)}
.tile:nth-child(4){background:linear-gradient(135deg,#1d5fb5,#3b8fd6 50%,#c99f93)}
.tile span{position:absolute;left:0;bottom:0;width:100%;height:48px;background:rgba(0,0,0,.5);color:var(--white);font-size:20px;font-weight:500;text-align:center;line-height:48px}

.services{position:absolute;top:1004px;left:0;width:1200px;height:426px;background:linear-gradient(135deg,#2f5f8c,#3a6b98 50%,#2c5a86);color:var(--white);text-align:center}
.services h2{position:absolute;top:57px;width:100%;font-size:26px;font-weight:400}
.service{position:absolute;top:130px;width:300px;margin-left:-150px}
.service .icon{margin:0 auto;width:100px;height:96px}
.service h3{margin-top:33px;font-size:20px;font-weight:400;letter-spacing:.5px}
.service p{margin-top:14px;font-size:12.5px;line-height:19px}
.service a{display:block;margin-top:16px;font-size:13px}

.blog{position:absolute;top:1430px;left:0;width:1200px;height:483px}
.blog h2{position:absolute;top:50px;width:100%;text-align:center;font-size:26px;font-weight:400;color:var(--ink)}
.blog h2 span{color:var(--brand)}
.post{position:absolute;top:111px;width:319px}
.post .thumb{height:196px;border:4px solid #eee;position:relative}
.post .date{position:absolute;left:0;top:55px;width:48px;color:var(--white);text-align:center}
.post .date .dm{background:var(--brand);height:52px;padding-top:7px;font-size:19px;line-height:20px}
.post .date .dm small{display:block;font-size:11px}
.post .date .yr{background:#333;height:34px;line-height:34px;font-size:14px}
.post h3{margin-top:17px;font-size:14.5px;font-weight:400;color:#333}
.post p{margin-top:10px;font-size:11px;line-height:17px;color:var(--muted);text-align:justify}
.post a{display:block;margin-top:12px;font-size:11.5px;color:var(--brand)}

.footer{position:absolute;top:1913px;left:0;width:1200px;height:212px;background:var(--footer);color:var(--white)}
.fcol{position:absolute;top:40px}
.fcol h4{font-size:16px;font-weight:400;letter-spacing:.3px;margin-bottom:22px}
.fcol p{font-size:12px;line-height:20px}
.fcol .line{display:flex;align-items:center;gap:12px;font-size:16px;margin-top:10px}
.fcol .line.small{font-size:13px;margin-top:6px}
.fcol .about{font-size:10.5px;line-height:18.5px;text-align:justify;width:250px}
.newsletter p{font-size:10.5px;line-height:19px;width:256px;text-align:justify}
.newsletter form{display:flex;margin-top:14px}
.newsletter input{width:171px;height:40px;border:0;padding:0 14px;font-size:10px;font-family:inherit}
.newsletter button{width:81px;height:40px;border:0;background:var(--brand);color:var(--white);font-size:14px;font-family:inherit}
.socials{display:flex;gap:20px}
.socials i{width:34px;height:34px;background:#eee;border-radius:4px;display:block}

.bottom{position:absolute;top:2125px;left:0;width:1200px;height:70px;background:var(--footer-bottom);border-top:1px solid #3a3a3a;color:var(--white);font-size:13px;text-align:center;line-height:30px;padding-top:5px}
</style>
</head>
<body>

<div class="topbar">
  <div class="contact">
    <span><svg width="12" height="12" viewBox="0 0 24 24"><rect x="1" y="1" width="22" height="22" rx="3" fill="#fff"/><path d="M8 6l2 3-1.5 1.5a8 8 0 0 0 5 5L15 14l3 2-1 2.5C11 18 6 13 5.5 7z" fill="#3a6a96"/></svg>: 0740219</span>
    <span><svg width="13" height="10" viewBox="0 0 26 20"><rect width="26" height="20" rx="2" fill="#fff"/><path d="M1 2l12 9 12-9" stroke="#3a6a96" stroke-width="2" fill="none"/></svg>: info@skyvoltbridge.net</span>
  </div>
  <svg class="search" width="15" height="15" viewBox="0 0 20 20"><circle cx="8" cy="8" r="6" stroke="#fff" stroke-width="2.5" fill="none"/><path d="M12.5 12.5L18 18" stroke="#fff" stroke-width="2.5"/></svg>
  <div class="divider"></div>
  <div class="social"><i></i><i></i><i></i><i></i></div>
</div>

<header class="header">
  <div class="brand"><i></i>skyvoltbridge</div>
  <nav class="nav">
    <a class="active" href="#">HOME</a><a href="#">ENGINEERING</a><a href="#">TESTING</a><a href="#">TRAINING</a><a href="#">HV BASICS</a><a href="#">ABOUT US</a><a href="#">CONTACT US</a>
  </nav>
</header>

<section class="hero" role="img" aria-label="Photo of an electric arc jumping between two high voltage spheres">
  <div class="arrow" style="left:58px"><svg width="30" height="30"><path d="M17 9l-6 6 6 6" stroke="#fff" stroke-width="2" fill="none"/></svg></div>
  <div class="arrow" style="left:1116px"><svg width="30" height="30"><path d="M13 9l6 6-6 6" stroke="#fff" stroke-width="2" fill="none"/></svg></div>
  <h1>HIGH VOLTAGE TRAINING</h1>
  <p>Operation and maintenance of HV systems</p>
</section>

<section class="tiles">
  <div class="tile" role="img" aria-label="Photo of electronic components on a circuit board"><span>CLEARANCES</span></div>
  <div class="tile" role="img" aria-label="Photo of a row of terminal blocks with wiring"><span>ELECTRICAL DISCHARGE</span></div>
  <div class="tile" role="img" aria-label="Photo of a lightning discharge"><span>PARTIAL DISCHARGE</span></div>
  <div class="tile" role="img" aria-label="Photo of a hand operating a test instrument"><span>HV TESTING</span></div>
</section>

<section class="services">
  <h2>OUR SERVICES</h2>
  <div class="service" style="left:256px">
    <svg class="icon" viewBox="0 0 100 96"><path d="M16 2H98L84 94H2Z" stroke="#fff" stroke-width="1.5" fill="none"/><circle cx="44" cy="52" r="11" stroke="#fff" stroke-width="6" stroke-dasharray="4 3" fill="none"/><circle cx="44" cy="52" r="4" fill="#fff"/><circle cx="62" cy="38" r="6" stroke="#fff" stroke-width="4" stroke-dasharray="3 2" fill="none"/><circle cx="62" cy="62" r="5" stroke="#fff" stroke-width="4" stroke-dasharray="3 2" fill="none"/></svg>
    <h3>ENGINEERING</h3>
    <p>Supporting the design of new HV systems and<br>components for use in aerospace environments</p>
    <a href="#">Learn More -&gt;</a>
  </div>
  <div class="service" style="left:610px">
    <svg class="icon" viewBox="0 0 100 96"><path d="M16 2H98L84 94H2Z" stroke="#fff" stroke-width="1.5" fill="none"/><path d="M54 30L42 52h9l-5 18 13-24h-9l5-16z" fill="#fff"/></svg>
    <h3>TESTING</h3>
    <p>Access to a full range of testing services to<br>validate the performance of HV systems</p>
    <a href="#">Learn More -&gt;</a>
  </div>
  <div class="service" style="left:963px">
    <svg class="icon" viewBox="0 0 100 96"><path d="M16 2H98L84 94H2Z" stroke="#fff" stroke-width="1.5" fill="none"/><circle cx="38" cy="38" r="6" fill="#fff"/><circle cx="62" cy="38" r="6" fill="#fff"/><circle cx="50" cy="42" r="7" fill="#fff"/><path d="M28 62c0-10 5-14 10-14s8 3 8 5h8c0-2 3-5 8-5s10 4 10 14z" fill="#fff"/></svg>
    <h3>TRAINING</h3>
    <p>Online and face to face training provision to<br>support your workforce</p>
    <a href="#">Learn More -&gt;</a>
  </div>
</section>

<section class="blog">
  <h2>LATEST <span>BLOG</span></h2>
  <article class="post" style="left:95px">
    <div class="thumb" role="img" aria-label="Photo of calipers, screwdrivers and a measuring tape on a drawing" style="background:linear-gradient(135deg,#e8e8e8,#c9c9c9 50%,#d63b2f)">
      <div class="date"><div class="dm">02<small>JUN</small></div><div class="yr">2016</div></div>
    </div>
    <h3>Neque porro quisquam est qui dolorem</h3>
    <p>Lorem Ipsum has been the industry's standard dummy text ever since the 1500s, when an unknown printer took a galley of type and scrambled it to make a type specimen book.</p>
    <a href="#">Read More »</a>
  </article>
  <article class="post" style="left:449px">
    <div class="thumb" role="img" aria-label="Photo of a laptop keyboard beside technical sheets" style="background:linear-gradient(135deg,#1f2a2a,#4a4a4a 50%,#d9d9d9)">
      <div class="date"><div class="dm">02<small>JUN</small></div><div class="yr">2016</div></div>
    </div>
    <h3>Neque porro quisquam est qui dolorem</h3>
    <p>Lorem Ipsum has been the industry's standard dummy text ever since the 1500s, when an unknown printer took a galley of type and scrambled it to make a type specimen book.</p>
    <a href="#">Read More »</a>
  </article>
  <article class="post" style="left:803px">
    <div class="thumb" role="img" aria-label="Photo of a blue test instrument with a display screen" style="background:linear-gradient(135deg,#1d3f9c,#3a5ec0 45%,#d8dde2)">
      <div class="date"><div class="dm">02<small>JUN</small></div><div class="yr">2016</div></div>
    </div>
    <h3>Neque porro quisquam est qui dolorem</h3>
    <p>Lorem Ipsum has been the industry's standard dummy text ever since the 1500s, when an unknown printer took a galley of type and scrambled it to make a type specimen book.</p>
    <a href="#">Read More »</a>
  </article>
</section>

<footer class="footer">
  <div class="fcol" style="left:91px">
    <h4>CONTACT US</h4>
    <p>48 Cedar Lane Brookfield NJ 08512<br>212 Ridge Avenue Suite 4<br>Brookfield NJ 08512</p>
    <div class="line"><svg width="16" height="16" viewBox="0 0 24 24"><path d="M6 2l4 5-2 2a12 12 0 0 0 7 7l2-2 5 4-2 3C10 21 3 14 3 5z" stroke="#fff" stroke-width="1.5" fill="none"/></svg>0740219</div>
    <div class="line small"><svg width="16" height="12" viewBox="0 0 26 20"><rect x="1" y="1" width="24" height="18" stroke="#fff" stroke-width="1.5" fill="none"/><path d="M1 1l12 10 12-10" stroke="#fff" stroke-width="1.5" fill="none"/></svg>info@skyvoltbridge.net</div>
  </div>
  <div class="fcol" style="left:364px">
    <h4>SKYVOLTBRIDGE</h4>
    <p class="about">skyvoltbridge can provide you with the engineering support you require as you develop new high voltage components and systems. With experience of cabling, connectors, electrical machines and power electronics we can help identify</p>
  </div>
  <div class="fcol newsletter" style="left:680px">
    <h4>NEWSLETTER</h4>
    <p>Excepteur sint occaecat cupidatat non proident, sunt in culpa qui officia deserunt mollit anim</p>
    <form><input type="email" placeholder="Enter your email address"><button type="button">Sign Up</button></form>
  </div>
  <div class="fcol" style="left:977px">
    <h4>SOCIAL MEDIA</h4>
    <div class="socials"><i></i><i></i><i></i></div>
  </div>
</footer>

<div class="bottom">2016 &nbsp;All Rights Reserved.</div>

</body>
</html>
```